Optometrist/Eye Care Clinic Business card with new logo attached

We are a small, independent eye care clinic in Canada. We have recently updated our logo (as attached), and would like a professional, modern and health care oriented business card to highlight our office details and our optometrist. We'd like to incorporate the blue colours as seen on our logo.

Target Market(s)

demographic: age 35-65 male/female equal

Industry/Entity Type

Health Care

Contact Information for Business Card

Name of clinic: "Marrow Bend Eye Care Optometry"

Font styles to use
Sans Serif

Colors
0355a3

Requirements
Must have
• our website: marrowbendeyecare.com
• Dr Lena Quorvik
• Optometrist
• 217-392 E Halvering Ave
• Vancouver BC V6R 3J8
• P: 604-319-2058
• E: info@marrowbendeyecare.com
Nice to have
• front side: logo/name of clinic as seen on logo attached and website
• backside: logo on the left side, and name/title/address/phone/email

```html
<!DOCTYPE html>
<html lang="en">
<head>
<meta charset="utf-8">
<title>Marrow Bend Eye Care Optometry – Business Cards</title>
<link href="https://fonts.googleapis.com/css2?family=Montserrat:wght@300;400;700&display=swap" rel="stylesheet">
<style>
  :root {
    --paper: #ffffff;
    --card-grey: #67686a;
    --edge: #b9babb;
    --brand-deep: #16435e;
    --rule: #6a6b6d;
    --copy: #6b6c6e;
    --copy-light: #9a9b9d;
  }
  * { margin: 0; padding: 0; box-sizing: border-box; }
  html, body {
    width: 960px; height: 1200px; overflow: hidden;
    background: var(--paper);
    font-family: "Montserrat", Arial, sans-serif;
  }
  .sheet { position: relative; width: 960px; height: 1200px; }

  .card {
    position: absolute;
    width: 382px; height: 233px;
    overflow: hidden;
    background: var(--paper);
    transform-origin: top left;
  }
  .card--front { border-radius: 26px 0 26px 0; }
  .card--back  { border-radius: 0 26px 0 26px; }
  .card--mini  { transform: scale(0.563); }

  .card__shape { position: absolute; inset: 0; width: 100%; height: 100%; }

  .brand { position: absolute; text-align: center; }
  .brand__mark { display: block; margin: 0 auto; border-radius: 50%; background: var(--brand-deep); }
  .brand__name {
    color: var(--brand-deep); font-weight: 400; letter-spacing: 0.18em;
    line-height: 1.3; text-transform: uppercase;
  }

  .card--front .brand { left: 91px; top: 38px; width: 200px; }
  .card--front .brand__mark { width: 100px; height: 100px; }
  .card--front .brand__name { margin-top: 16px; font-size: 17px; }

  .website {
    position: absolute; right: 38px; bottom: 4px;
    color: var(--paper); font-size: 8.5px; font-weight: 400;
  }

  .card--back .brand { left: 10px; top: 51px; width: 115px; }
  .card--back .brand__mark { width: 68px; height: 68px; }
  .card--back .brand__name { margin-top: 8px; font-size: 9.5px; letter-spacing: 0.12em; }

  .divider { position: absolute; left: 134px; top: 9px; width: 2px; height: 211px; background: var(--rule); }

  .person { position: absolute; left: 143px; top: 80px; width: 235px; }
  .person__name { color: var(--brand-deep); font-weight: 700; font-size: 21px; line-height: 1; white-space: nowrap; }
  .person__title { color: var(--copy); font-weight: 300; font-size: 15px; line-height: 1.1; text-align: center; width: 225px; }

  .contact { position: absolute; left: 143px; top: 154px; color: var(--copy); font-weight: 300; }
  .contact__line { font-size: 14.5px; line-height: 20px; white-space: nowrap; }
  .contact__line--email { font-size: 12.5px; line-height: 16px; color: var(--copy-light); }
</style>
</head>
<body>
<main class="sheet">

  <!-- Front, small preview -->
  <section class="card card--front card--mini" style="left:240px; top:120px;">
    <svg class="card__shape" viewBox="0 0 382 233" preserveAspectRatio="none" aria-hidden="true">
      <path d="M0 0 H228 C126 51 25 127 2 233 H0 Z" fill="var(--card-grey)"/>
      <path d="M382 0 C363 93 278 186 160 233 H382 Z" fill="var(--card-grey)"/>
      <rect x="0.5" y="0.5" width="381" height="232" rx="0" fill="none" stroke="var(--edge)"/>
    </svg>
    <div class="brand">
      <span class="brand__mark"></span>
      <p class="brand__name">Marrow Bend<br>Eye Care<br>Optometry</p>
    </div>
    <p class="website">website: marrowbendeyecare.com</p>
  </section>

  <!-- Back, small preview -->
  <section class="card card--back card--mini" style="left:492px; top:124px;">
    <svg class="card__shape" viewBox="0 0 382 233" preserveAspectRatio="none" aria-hidden="true">
      <path d="M154 0 H382 V233 C371 126 287 25 154 0 Z" fill="var(--card-grey)"/>
      <rect x="0.5" y="0.5" width="381" height="232" fill="none" stroke="var(--edge)"/>
    </svg>
    <div class="brand">
      <span class="brand__mark"></span>
      <p class="brand__name">Marrow Bend<br>Eye Care<br>Optometry</p>
    </div>
    <span class="divider"></span>
    <div class="person">
      <p class="person__name">DR. LENA QUORVIK</p>
      <p class="person__title">OPTOMETRIST</p>
    </div>
    <div class="contact">
      <p class="contact__line">217-392 E Halvering Ave</p>
      <p class="contact__line">Vancouver BC V6R 3J8</p>
      <p class="contact__line">Phone: 604-319-2058</p>
      <p class="contact__line contact__line--email">E: info@marrowbendeyecare.com</p>
    </div>
  </section>

  <!-- Front, full size -->
  <section class="card card--front" style="left:276px; top:444px;">
    <svg class="card__shape" viewBox="0 0 382 233" preserveAspectRatio="none" aria-hidden="true">
      <path d="M0 0 H228 C126 51 25 127 2 233 H0 Z" fill="var(--card-grey)"/>
      <path d="M382 0 C363 93 278 186 160 233 H382 Z" fill="var(--card-grey)"/>
      <rect x="0.5" y="0.5" width="381" height="232" fill="none" stroke="var(--edge)"/>
    </svg>
    <div class="brand">
      <span class="brand__mark"></span>
      <p class="brand__name">Marrow Bend<br>Eye Care<br>Optometry</p>
    </div>
    <p class="website">website: marrowbendeyecare.com</p>
  </section>

  <!-- Back, full size -->
  <section class="card card--back" style="left:277px; top:723px;">
    <svg class="card__shape" viewBox="0 0 382 233" preserveAspectRatio="none" aria-hidden="true">
      <path d="M154 0 H382 V233 C371 126 287 25 154 0 Z" fill="var(--card-grey)"/>
      <rect x="0.5" y="0.5" width="381" height="232" fill="none" stroke="var(--edge)"/>
    </svg>
    <div class="brand">
      <span class="brand__mark"></span>
      <p class="brand__name">Marrow Bend<br>Eye Care<br>Optometry</p>
    </div>
    <span class="divider"></span>
    <div class="person">
      <p class="person__name">DR. LENA QUORVIK</p>
      <p class="person__title">OPTOMETRIST</p>
    </div>
    <div class="contact">
      <p class="contact__line">217-392 E Halvering Ave</p>
      <p class="contact__line">Vancouver BC V6R 3J8</p>
      <p class="contact__line">Phone: 604-319-2058</p>
      <p class="contact__line contact__line--email">E: info@marrowbendeyecare.com</p>
    </div>
  </section>

</main>
</body>
</html>
```